Team Member Spotlight 'Stats Card' Design for ProfilNet

We are creating a 'Stats Card'-style team member spotlight post for our company's ProfilNet page. The design should be professional yet fun, reflecting our company's approachable and innovative brand. Here’s what we need:

Header featuring:
Name: Reed Calloway
Role: Area Sales Manager - Austin, TX
Photo: Will provide
Quick stats section with bold, modern fonts:
Years in Pain Management: 8 years
Time at OKRA VENT QS: 1 year (by February)
Favorite Quote: “Nothing in the world can take the place of persistence.” – Ambrose Thistlewood
Hobby/Passion: Making music (on Tunevault as Reed Calloway!)
Football Team: Pelham Tech (Herons)

Use vibrant, approachable company branding colors.
Incorporate small themed icons (e.g., music notes, football elements).
Clean, modern layout with clear sections and engaging visuals.
Subtle background details that hint at music and Texas without overpowering the content.

Optimized for ProfilNet dimensions (square or portrait format).
Delivered in editable file formats (Canva) for future use.

Professional but approachable.
Engaging design that will catch attention while staying on-brand.
We will provide the company branding guide, Reed’s photo, and detailed stats. The design should feel cohesive with our brand and stand out on ProfilNet.

Industry/Entity Type

Medical Device / Physicians

Colors

Designer to choose colors to be used in the design.

Requirements
Must have
• Include OKRA VENT QS logo & Company Colors: #a9218f & #011842

```html
<!DOCTYPE html>
<html lang="en">
<head>
<meta charset="utf-8">
<title>Team Spotlight – Reed Calloway</title>
<link rel="stylesheet" href="https://fonts.googleapis.com/css2?family=Montserrat:wght@700;800;900&display=swap">
<style>
  :root {
    --brand-purple: #a9218f;
    --brand-navy: #011842;
    --white: #ffffff;
    --photo-base: #c9ccd4;
    --photo-suit: #2a3f6b;
    --badge-tone: #c8294a;
  }
  * { margin: 0; padding: 0; box-sizing: border-box; }
  html, body { width: 774px; height: 1200px; overflow: hidden; background: var(--white); }
  .card {
    position: relative; width: 774px; height: 1200px;
    background: var(--brand-purple); border-radius: 10px; overflow: hidden;
    font-family: "Montserrat", Arial, sans-serif; color: var(--white);
  }
  .panel { position: absolute; background: var(--brand-navy); }
  .panel--side { left: 392px; top: 170px; width: 370px; height: 470px; }
  .panel--stats { left: 12px; top: 508px; width: 750px; height: 680px; border-radius: 0 0 6px 6px; }
  .logo-box {
    position: absolute; left: 392px; top: 11px; width: 369px; height: 163px;
    background: var(--white); display: flex; align-items: center; justify-content: center;
  }
  .logo-name { font-weight: 800; font-size: 40px; letter-spacing: 1px; color: var(--brand-navy); }
  .portrait-ring {
    position: absolute; left: 207px; top: 194px; width: 410px; height: 410px;
    border-radius: 50%; background: var(--brand-purple);
  }
  .portrait {
    position: absolute; left: 227px; top: 214px; width: 370px; height: 370px; border-radius: 50%;
    background: linear-gradient(180deg, var(--photo-base) 0%, #b7b9bf 55%, var(--photo-suit) 56%, #1f3360 100%);
  }
  .member-name {
    position: absolute; left: 49px; top: 25px; z-index: 2;
    font-weight: 900; font-size: 56px; line-height: 84px; letter-spacing: -1px;
  }
  .member-name span { display: block; }
  .name-rule { position: absolute; left: 49px; top: 208px; width: 252px; height: 2px; background: var(--white); z-index: 2; }
  .member-role {
    position: absolute; left: 49px; top: 224px; z-index: 2;
    font-weight: 800; font-size: 18px; line-height: 29px; letter-spacing: 0.2px;
  }
  .city-badge {
    position: absolute; left: 96px; top: 322px; width: 84px; height: 84px;
    border-radius: 50%; background: var(--badge-tone);
  }
  .themed-icons { position: absolute; left: 560px; top: 185px; }
  .stats-banner { position: absolute; left: 171px; top: 632px; }
  .stats-banner__label {
    position: absolute; left: 171px; top: 632px; width: 430px; height: 54px;
    display: flex; align-items: center; justify-content: center;
    font-weight: 900; font-size: 39px; letter-spacing: 0.5px;
  }
  .stat {
    position: absolute; left: 53px; font-weight: 900; font-size: 26px;
    line-height: 36px; white-space: nowrap;
  }
  .stat--quote { font-size: 23px; }
  .stat-rule { position: absolute; left: 58px; width: 661px; height: 1.5px; background: var(--white); }
</style>
</head>
<body>
<main class="card">
  <div class="panel panel--side"></div>
  <div class="panel panel--stats"></div>

  <div class="logo-box"><span class="logo-name">OKRA VENT QS</span></div>

  <div class="portrait-ring"></div>
  <div class="portrait" role="img" aria-label="Portrait photo of Reed Calloway in a navy suit and tie"></div>

  <h1 class="member-name"><span>REED</span><span>CALLOWAY</span></h1>
  <div class="name-rule"></div>
  <p class="member-role">AREA SALES MANAGER<br>- AUSTIN, TX</p>

  <div class="city-badge" role="img" aria-label="City emblem"></div>

  <svg class="themed-icons" width="120" height="440" viewBox="0 0 120 440" fill="none" stroke="var(--white)" stroke-width="4" stroke-linecap="round" stroke-linejoin="round">
    <path d="M12 6 V60 H78"/>
    <path d="M18 52 L34 38 L46 44 L72 18"/>
    <path d="M60 16 H76 V32"/>
    <g fill="var(--white)" stroke="none">
      <ellipse cx="62" cy="130" rx="10" ry="8" transform="rotate(-20 62 130)"/>
      <ellipse cx="88" cy="122" rx="10" ry="8" transform="rotate(-20 88 122)"/>
      <rect x="69" y="84" width="4" height="46"/>
      <rect x="95" y="76" width="4" height="46"/>
      <path d="M69 84 L99 76 V86 L69 94 Z"/>
      <ellipse cx="96" cy="204" rx="10" ry="8" transform="rotate(-20 96 204)"/>
      <rect x="103" y="158" width="4" height="46"/>
      <path d="M107 158 C112 170 122 174 116 190 C118 176 112 172 107 170 Z"/>
      <ellipse cx="66" cy="290" rx="10" ry="8" transform="rotate(-20 66 290)"/>
      <rect x="73" y="244" width="4" height="46"/>
    </g>
    <g transform="translate(50 395) rotate(-30)">
      <ellipse cx="0" cy="0" rx="44" ry="24" fill="var(--white)" stroke="none"/>
      <path d="M-24 0 H24" stroke="var(--brand-navy)" stroke-width="2.5"/>
      <path d="M-18 -5 V5 M-10 -5 V5 M-2 -5 V5 M6 -5 V5 M14 -5 V5" stroke="var(--brand-navy)" stroke-width="2"/>
      <path d="M-30 -16 Q-36 0 -30 16 M30 -16 Q36 0 30 16" stroke="var(--brand-navy)" stroke-width="2.5"/>
    </g>
  </svg>

  <svg class="stats-banner" width="603" height="54" viewBox="0 0 603 54">
    <path d="M0 0 H603 V54 H24 Z" fill="var(--brand-purple)"/>
  </svg>
  <h2 class="stats-banner__label">QUICK STATS</h2>

  <p class="stat" style="top:711px">YEARS IN PAIN MANAGEMENT: 8 YEARS</p>
  <div class="stat-rule" style="top:764px"></div>
  <p class="stat" style="top:786px">TIME AT OKRA VENT QS: 1 YEAR (BY FEBRUARY)</p>
  <div class="stat-rule" style="top:843px"></div>
  <p class="stat stat--quote" style="top:863px">FAVORITE QUOTE:<br>“NOTHING IN THE WORLD CAN TAKE THE<br>PLACE OF PERSISTENCE.” – AMBROSE THISTLEWOOD</p>
  <div class="stat-rule" style="top:985px"></div>
  <p class="stat" style="top:1002px">HOBBY/PASSION: MAKING MUSIC (ON<br>TUNEVAULT AS REED CALLOWAY!)</p>
  <div class="stat-rule" style="top:1089px"></div>
  <p class="stat" style="top:1112px">FOOTBALL TEAM: PELHAM TECH (HERONS)</p>
</main>
</body>
</html>
```